Junk Removal company with existing WordPress website needs new mobile enhanced website

I am looking to have someone take my existing website and either update it with a new design and menu which is more mobile enhanced (70% of my traffic is from mobile devices and most people stay on the home page to find what they need) or create a new website from scratch to achieve my design goals. My name goal is the have to home page be quick and easy to find what the customer is looking for.
Our current website is: BrightmoorJunkCarters.com and plain rating badge my business page https://g.page/brightmoorjunkcarters
I have attached an example the design idea I came up with for the home page based on what I would like it to look like as well as some logo files and pictures.

```html
<!DOCTYPE html>
<html lang="en">
<head>
<meta charset="utf-8">
<title>Brightmoor Junk Carters</title>
<link rel="stylesheet" href="https://fonts.googleapis.com/css2?family=Poppins:wght@400;500;600;700;800&family=Open+Sans:wght@400;600&display=swap">
<style>
:root{
  --orange:#f7941d;
  --yellow:#f9b233;
  --red:#e2261c;
  --dark:#1e1e1e;
  --dark2:#2a2a2a;
  --ink:#222;
  --muted:#666;
  --white:#fff;
  --line:#e5e5e5;
}
*{box-sizing:border-box;margin:0;padding:0}
html,body{width:1200px;height:3672px;overflow:hidden}
body{font-family:"Open Sans",Arial,sans-serif;color:var(--ink);background:#fff;position:relative}
h1,h2,h3,h4,.brand,.nav a{font-family:"Poppins",Arial,sans-serif}
.abs{position:absolute}

/* header */
.site-header{position:absolute;left:0;top:0;width:1200px;height:80px;background:#fff;box-shadow:0 2px 8px rgba(0,0,0,.12);z-index:5}
.brand{position:absolute;left:60px;top:14px;display:flex;align-items:center;gap:10px;font-weight:800;font-size:18px;color:var(--red);line-height:1}
.brand .mark{width:44px;height:44px;background:var(--dark);border-radius:50%}
.top-contact{position:absolute;left:520px;top:8px;font-size:12px;color:var(--muted);display:flex;gap:24px}
.top-contact span{color:var(--red)}
.nav{position:absolute;left:420px;top:44px;display:flex;gap:34px}
.nav a{font-size:12px;font-weight:600;color:var(--ink);text-decoration:none;text-transform:uppercase}
.nav a.active{color:var(--orange);border-bottom:2px solid var(--orange);padding-bottom:4px}
.rating-badge{position:absolute;right:60px;top:12px;width:96px;height:54px;background:#f3f3f3;border:1px solid var(--line);border-radius:4px}

/* hero */
.hero{position:absolute;left:0;top:80px;width:1200px;height:440px;overflow:hidden}
.hero-photo{position:absolute;inset:0;background:linear-gradient(180deg,#5d6c78 0%,#3d4650 55%,#2e3338 100%)}
.hero-shade{position:absolute;inset:0;background:rgba(0,0,0,.25)}
.hero h1{position:absolute;left:0;right:0;top:150px;text-align:center;color:#fff;font-size:36px;font-weight:700;line-height:1.3;text-shadow:0 2px 6px rgba(0,0,0,.5)}
.hero-dots{position:absolute;left:116px;top:418px;display:flex;gap:6px}
.hero-dots i{width:14px;height:14px;border-radius:50%;background:#fff;display:block}
.hero-dots i.on{background:var(--orange)}
.hero-band{position:absolute;left:0;top:480px;width:1200px}

/* services */
.services{position:absolute;left:0;top:560px;width:1200px;height:600px}
.service-card{position:absolute;top:0;width:250px;height:570px;background:#fff;box-shadow:0 4px 14px rgba(0,0,0,.14);text-align:center;padding-top:16px}
.service-card .hex{width:170px;height:190px;margin:0 auto;clip-path:polygon(50% 0,100% 25%,100% 75%,50% 100%,0 75%,0 25%);background:var(--orange);padding:6px}
.service-card .hex div{width:100%;height:100%;clip-path:polygon(50% 0,100% 25%,100% 75%,50% 100%,0 75%,0 25%)}
.service-card h3{color:var(--orange);font-size:24px;font-weight:700;line-height:1.15;margin-top:18px}
.service-card ul{list-style:none;text-align:left;margin:18px 0 0 34px;font-size:13px;line-height:1.95;color:#333}
.service-card li::before{content:"";display:inline-block;width:6px;height:6px;background:var(--orange);border-radius:50%;margin-right:8px;vertical-align:middle}

/* pricing */
.pricing{position:absolute;left:0;top:1180px;width:1200px;height:600px;background:var(--dark)}
.pricing h2{position:absolute;left:80px;top:60px;color:#fff;font-size:36px;font-weight:700}
.pricing h2::after{content:"";display:block;width:60px;height:4px;background:var(--orange);margin-top:8px}
.price-list{position:absolute;left:80px;top:150px;width:440px}
.price-list h4{color:var(--orange);font-size:14px;font-weight:700;margin-top:14px}
.price-list p{color:#ddd;font-size:12px;line-height:1.55}
.price-photo{position:absolute;left:620px;top:140px;width:500px;height:340px;border:6px solid #fff;background:linear-gradient(135deg,#7d8a95,#4a5560 60%,#2f363d)}

/* process */
.process{position:absolute;left:0;top:1780px;width:1200px;height:420px;text-align:center}
.process .kicker{margin-top:40px;font-family:"Poppins",sans-serif;font-size:18px;font-weight:600}
.process h2{color:var(--red);font-size:34px;font-weight:800;line-height:1.2}
.process .sub{font-family:"Poppins",sans-serif;font-weight:600;font-size:16px}
.steps{display:flex;justify-content:center;gap:40px;margin-top:30px}
.step{width:280px;height:170px;background:#fff;box-shadow:0 4px 14px rgba(0,0,0,.12);display:flex;gap:16px;padding:26px 20px;text-align:left}
.step .icon{width:56px;height:56px;background:var(--red);border-radius:6px;flex:none;display:flex;align-items:center;justify-content:center}
.step h4{font-size:18px;color:var(--red);font-weight:700}
.step p{font-size:12px;line-height:1.5;color:#444;margin-top:4px}
.step .btn{display:inline-block;margin-top:8px;background:var(--red);color:#fff;font-size:11px;padding:4px 12px;border-radius:3px;font-weight:600}

/* trucks */
.trucks{position:absolute;left:0;top:2180px;width:1200px;height:540px;background:var(--dark)}
.trucks h2{position:absolute;left:0;right:0;top:80px;text-align:center;color:var(--red);font-size:40px;font-weight:800}
.trucks .lead{position:absolute;left:230px;width:740px;top:150px;text-align:center;color:#eee;font-size:14px;line-height:1.6}
.truck-card{position:absolute;top:300px;width:290px;height:170px;background:#fff}
.truck-card .photo{height:124px;margin:8px;background:linear-gradient(180deg,#f4f4f4,#d9dde0)}
.truck-card .specs{position:absolute;left:0;right:0;bottom:0;height:38px;display:flex}
.truck-card .specs span{flex:1;font-size:10px;color:#fff;font-weight:600;display:flex;align-items:center;justify-content:center;text-align:center;line-height:1.2;border-right:1px solid rgba(255,255,255,.4)}
.truck-card .specs span:nth-child(odd){background:var(--orange)}
.truck-card .specs span:nth-child(even){background:var(--red)}

/* map */
.map{position:absolute;left:0;top:2720px;width:1200px;height:560px;background:linear-gradient(160deg,#eceff1,#dfe4e6)}

/* footer */
.site-footer{position:absolute;left:0;top:3280px;width:1200px;height:360px;background:var(--dark)}
.foot-col{position:absolute;top:60px}
.foot-col h4{color:var(--orange);font-size:20px;font-weight:700;margin-bottom:16px}
.foot-col li{list-style:none;color:#ddd;font-size:14px;line-height:2}
.copyright{position:absolute;left:0;top:3640px;width:1200px;height:32px;background:var(--red);color:#fff;font-size:12px;padding:8px 40px}
.social{position:absolute;right:40px;top:8px;display:flex;gap:10px}
.social i{display:block;width:16px;height:16px;background:#fff;border-radius:3px}
</style>
</head>
<body>

<header class="site-header">
  <div class="brand"><span class="mark"></span>Brightmoor Junk Carters</div>
  <div class="top-contact"><div><span>&#9742;</span> (555) 014-2290</div><div><span>&#9993;</span> info@brightmoorjunk.com</div></div>
  <nav class="nav">
    <a class="active" href="#">Home</a><a href="#">Our Services</a><a href="#">What We Take</a><a href="#">Service Areas</a><a href="#">Contact Us</a>
  </nav>
  <div class="rating-badge"></div>
</header>

<section class="hero">
  <div class="hero-photo" role="img" aria-label="Company junk removal trucks parked in front of a house"></div>
  <div class="hero-shade"></div>
  <h1>Best Rated Junk Removal &amp;<br>Property Cleanout Company in<br>The Brightmoor Valley</h1>
  <div class="hero-dots"><i></i><i class="on"></i></div>
  <svg class="hero-band" width="1200" height="40" viewBox="0 0 1200 40"><polygon points="0,30 1200,0 1200,40 0,40" fill="#fff"/><polygon points="0,24 1200,-6 1200,4 0,34" fill="#f9b233"/></svg>
</section>

<section class="services">
  <article class="service-card" style="left:130px">
    <div class="hex"><div role="img" aria-label="Pile of household junk" style="background:linear-gradient(135deg,#6aa0c8,#c04a3a)"></div></div>
    <h3>Junk<br>Removal</h3>
    <ul><li>Junk Removal &amp; Hauling</li><li>Furniture Removal</li><li>Appliance Removal</li><li>Hot Tub Removal</li><li>Yard Debris Removal</li><li>Remodeling Debris Removal</li><li>Construction Debris Removal</li><li>Play Structure Removal</li></ul>
  </article>
  <article class="service-card" style="left:400px">
    <div class="hex"><div role="img" aria-label="Cluttered garage ready for cleanout" style="background:linear-gradient(135deg,#8a6a4a,#3f6e8c)"></div></div>
    <h3>Property<br>Cleanout</h3>
    <ul><li>Estate Cleanouts</li><li>Residential Cleanouts</li><li>Garage Cleanouts</li><li>Storage Unit Cleanouts</li><li>Foreclosure Cleanouts</li><li>Hoarder Cleanouts</li><li>Attic/Basement Cleanouts</li><li>Business/Office Cleanouts</li></ul>
  </article>
  <article class="service-card" style="left:670px">
    <div class="hex"><div role="img" aria-label="Old shed being torn down" style="background:linear-gradient(135deg,#9b7b5a,#5a4a3a)"></div></div>
    <h3>Light<br>Demolition</h3>
    <ul><li>Shed Removal</li><li>Fence Removal</li><li>Deck Removal</li><li>Playsets/Swingset Removal</li><li>Gazebo Removal</li><li>Above Ground Pool Removal</li><li>Misc. Structure Removal</li></ul>
  </article>
  <article class="service-card" style="left:940px">
    <div class="hex"><div role="img" aria-label="Dumpster trailer parked on a driveway" style="background:linear-gradient(135deg,#6c7a86,#2f3438)"></div></div>
    <h3>Dumpster<br>Rental</h3>
    <ul><li>24 Hour Rental</li><li>48 Hour Rental</li><li>72 Hour Rental</li><li>Weekly Rental</li></ul>
  </article>
</section>

<svg class="abs" style="left:0;top:1150px" width="1200" height="40" viewBox="0 0 1200 40"><polygon points="0,40 1200,10 1200,40" fill="#1e1e1e"/><polygon points="0,34 1200,4 1200,14 0,44" fill="#f7941d"/></svg>

<section class="pricing">
  <h2>How We Price</h2>
  <div class="price-list">
    <h4>Volume Based Pricing</h4>
    <p>Our pricing is based on the amount of space your items take up in our truck.</p>
    <h4>Minimum Loads</h4>
    <p>Our pricing starts at minimum pickup fee and goes up through twelve different price points to a full load rate.</p>
    <h4>Free Estimates</h4>
    <p>We can provide a free estimate over the phone, text or email so you know a price range before we show up.</p>
    <h4>Upfront Pricing</h4>
    <p>We always provide our valued customers with a firm price on site before we begin a job.</p>
    <h4>No Hidden Fees</h4>
    <p>All fuel, labor and disposal fees are included in your upfront pricing.</p>
  </div>
  <div class="price-photo" role="img" aria-label="Crew member standing beside a box truck"></div>
</section>

<section class="process">
  <p class="kicker">3 Simple Ways to Get your Estimate Today!</p>
  <h2>We make the Process</h2>
  <p class="sub">Quick &amp; Easy</p>
  <div class="steps">
    <div class="step">
      <div class="icon"><svg width="28" height="28" viewBox="0 0 24 24"><path d="M6.6 10.8a15 15 0 006.6 6.6l2.2-2.2c.3-.3.7-.4 1-.2 1.1.4 2.3.6 3.6.6.6 0 1 .4 1 1V20c0 .6-.4 1-1 1A17 17 0 013 4c0-.6.4-1 1-1h3.5c.6 0 1 .4 1 1 0 1.3.2 2.5.6 3.6.1.3 0 .7-.2 1z" fill="#fff"/></svg></div>
      <div><h4>Call Us</h4><p>Today and talk to one of our friendly, local staff members.</p></div>
    </div>
    <div class="step">
      <div class="icon"><svg width="28" height="28" viewBox="0 0 24 24"><path d="M4 4h16v12H8l-4 4z" fill="#fff"/></svg></div>
      <div><h4>Text Us</h4><p>Today with photos of the stuff you would like removed.</p><span class="btn">Text Us</span></div>
    </div>
    <div class="step">
      <div class="icon"><svg width="28" height="28" viewBox="0 0 24 24"><rect x="3" y="5" width="18" height="14" rx="1" fill="#fff"/><path d="M3 6l9 7 9-7" stroke="#e2261c" stroke-width="2" fill="none"/></svg></div>
      <div><h4>Email Us</h4><p>Email us today what you would like us to haul away.</p></div>
    </div>
  </div>
</section>

<section class="trucks">
  <svg class="abs" style="left:0;top:0" width="1200" height="40" viewBox="0 0 1200 40"><polygon points="0,0 1200,0 1200,14 0,34" fill="#fff"/><polygon points="0,30 1200,10 1200,20 0,40" fill="#f7941d"/></svg>
  <h2>Bigger Truck, Better Pricing!</h2>
  <p class="lead">Brightmoor Junk Carters is a local family owned and operated business and not a large national franchise. That means we don't have to pass along the 10 - 15% franchise fee on to our customers like our competition!</p>
  <div class="truck-card" style="left:160px"><div class="photo" role="img" aria-label="Our large box truck"></div><div class="specs"><span>Box truck</span><span>20 cubic yards</span><span>Full load</span></div></div>
  <div class="truck-card" style="left:455px"><div class="photo" role="img" aria-label="Typical competitor truck"></div><div class="specs"><span>Competitor</span><span>15 cubic yards</span><span>Full load</span></div></div>
  <div class="truck-card" style="left:750px"><div class="photo" role="img" aria-label="Small competitor truck"></div><div class="specs"><span>Competitor</span><span>12 cubic yards</span><span>Full load</span></div></div>
</section>

<section class="map" role="img" aria-label="Street map showing the company location">
  <svg class="abs" style="left:584px;top:250px" width="32" height="44" viewBox="0 0 24 34"><path d="M12 0C5.4 0 0 5.2 0 11.7 0 20.5 12 34 12 34s12-13.5 12-22.3C24 5.2 18.6 0 12 0z" fill="#e2261c"/><circle cx="12" cy="12" r="4.5" fill="#fff"/></svg>
</section>

<footer class="site-footer">
  <div class="foot-col" style="left:340px"><h4>Quick Link</h4><ul><li>Home</li><li>What We Take</li><li>Service Areas</li><li>Contact Us</li></ul></div>
  <div class="foot-col" style="left:600px"><h4>Our Services</h4><ul><li>Junk Removal &amp; Hauling</li><li>Property Cleanout</li><li>Light Demolition</li><li>Dumpster Rental</li></ul></div>
  <div class="foot-col" style="left:860px;width:280px"><h4>Contact Info</h4><ul><li>&#9906; 1420 Cedar Mill Road,<br>&nbsp;&nbsp;&nbsp;Brightmoor, ID 83700</li><li>&#9742; (555) 014-2290</li><li>&#9993; info@brightmoorjunk.com</li></ul></div>
</footer>
<div class="copyright">Copyright © Brightmoor Junk Carters. All Rights Reserved.<div class="social"><i></i><i></i></div></div>

</body>
</html>
```